Professional BIO Template with photo and logo

Hello,
I need a professional Bio template developed via Microsoft WORD ASAP!!!!! I would like to just be able to add the text I need to add. So resize-able text boxes. Potentially able to adjust the font. These are the things I need added it to include.
Head shot (attached)
Text Box for Name
Text Box for phone number
Text box for email
KTW Logo (attached)
Maybe a blue banner at the top or some background boxes that are blue or grey. Here are the pantone colors that our company uses.

CORE COLOR
100c 91m 17y 6k 38r 58g 128b Hex #263A80 Pantone 7687 C

CORE CONTRAST COLOR
36c 29m 28y 0k 168r 168g 170b Hex #669999 Pantone Cool Gray 6C

I also attached some examples of what we have been looking at. Instead of green add the blue...instead of black maybe just be white.

Thank you

```html
<!DOCTYPE html>
<html lang="en">
<head>
<meta charset="utf-8">
<title>Dana Whitfield – Marketing Manager</title>
<link href="https://fonts.googleapis.com/css2?family=Montserrat:wght@400;600;700&family=Open+Sans:wght@600;700&family=Lato:wght@400;700&display=swap" rel="stylesheet">
<style>
  :root {
    --core-blue: #263A80;
    --panel-grey: #EFEFF1;
    --rule-grey: #C8C8CA;
    --text-dark: #3A3A3C;
    --text-body: #4A4A4C;
    --text-soft: #77777A;
    --backdrop: #DCDCDE;
    --white: #FFFFFF;
  }
  * { margin: 0; padding: 0; box-sizing: border-box; }
  html, body { width: 991px; height: 1200px; overflow: hidden; }
  body { background: var(--backdrop); position: relative; font-family: 'Lato', sans-serif; }

  .resume {
    position: absolute; left: 82px; top: 20px;
    width: 827px; height: 1160px;
    background: var(--white); overflow: hidden;
    box-shadow: 0 4px 14px rgba(0,0,0,0.18);
  }
  .header-band { position: absolute; left: 0; top: 0; width: 827px; height: 255px; background: var(--core-blue); }
  .main-panel { position: absolute; left: 317px; top: 255px; width: 510px; height: 905px; background: var(--panel-grey); }
  .accent-bar-right { position: absolute; left: 799px; top: 471px; width: 28px; height: 342px; background: var(--core-blue); }
  .accent-bar-left { position: absolute; left: 0; top: 954px; width: 28px; height: 206px; background: var(--core-blue); }

  .photo-frame { position: absolute; left: 57px; top: 78px; width: 217px; height: 241px; background: var(--white); padding: 8px 7px; }
  .headshot { width: 100%; height: 100%; background: radial-gradient(ellipse at 50% 40%, #6b6b6e 0%, #48484b 55%, #2e2e31 100%); }

  .name { position: absolute; left: 345px; top: 80px; font-family: 'Montserrat', sans-serif; color: var(--white); font-size: 58px; line-height: 62px; letter-spacing: 0.5px; }
  .name .first { font-weight: 700; display: block; }
  .name .last { font-weight: 400; display: block; }
  .title-rule { position: absolute; left: 502px; top: 207px; width: 352px; height: 1.5px; background: var(--white); left: 502px; }
  .job-title { position: absolute; left: 502px; top: 222px; font-family: 'Montserrat', sans-serif; font-weight: 400; color: var(--white); font-size: 20px; letter-spacing: 0.33em; white-space: nowrap; }

  .side-heading { position: absolute; left: 57px; font-family: 'Open Sans', sans-serif; font-weight: 700; color: var(--core-blue); font-size: 20px; line-height: 24px; }
  .side-rule { position: absolute; left: 57px; height: 1.5px; background: var(--rule-grey); }

  .about-text { position: absolute; left: 57px; top: 379px; width: 215px; font-size: 11.2px; line-height: 18.4px; color: var(--text-body); text-align: justify; }
  .about-text p + p { margin-top: 18.4px; }

  .language-list { position: absolute; left: 57px; top: 725px; width: 199px; list-style: none; font-size: 11.5px; line-height: 20.5px; color: var(--text-body); }
  .language-list li { display: flex; justify-content: space-between; }

  .contact-list { position: absolute; left: 60px; top: 862px; list-style: none; font-size: 13.5px; color: var(--text-body); }
  .contact-list li { height: 27px; line-height: 20px; }
  .contact-list li:nth-child(2) { margin-top: 2px; }

  .company-mark { position: absolute; left: 60px; top: 1048px; display: flex; align-items: center; gap: 10px; }
  .company-mark .mark-square { width: 22px; height: 22px; background: var(--core-blue); }
  .company-mark .mark-name { font-family: 'Open Sans', sans-serif; font-weight: 700; font-size: 34px; line-height: 40px; color: var(--core-blue); letter-spacing: 2px; }

  .section-heading { position: absolute; left: 344px; display: flex; align-items: center; gap: 10px; font-family: 'Open Sans', sans-serif; font-weight: 600; font-size: 20px; color: var(--text-dark); }
  .section-heading svg { width: 28px; height: 28px; display: block; }
  .section-rule { position: absolute; left: 339px; width: 434px; height: 1.5px; background: var(--rule-grey); }

  .entry { position: absolute; left: 344px; width: 430px; }
  .entry .label { position: absolute; left: 0; top: 0; font-size: 12.5px; line-height: 16px; color: var(--text-dark); }
  .entry .years { position: absolute; left: 0; top: 22px; font-size: 12px; line-height: 16px; color: var(--text-body); letter-spacing: 0.3px; }
  .entry .role { position: absolute; left: 146px; top: 0; font-size: 12.5px; line-height: 16px; font-weight: 700; color: var(--text-dark); white-space: nowrap; }
  .entry .detail { position: absolute; left: 146px; top: 22px; width: 280px; font-size: 10.9px; line-height: 15.2px; color: var(--text-soft); }
  .education .role, .education .detail { left: 141px; }
</style>
</head>
<body>
  <main class="resume">
    <div class="header-band"></div>
    <div class="main-panel"></div>
    <div class="accent-bar-right"></div>
    <div class="accent-bar-left"></div>

    <div class="photo-frame">
      <div class="headshot" role="img" aria-label="Head shot of the marketing manager in a dark suit against a grey backdrop"></div>
    </div>

    <h1 class="name"><span class="first">DANA</span><span class="last">WHITFIELD</span></h1>
    <div class="title-rule" style="left:345px"></div>
    <p class="job-title" style="left:345px">MARKETING MANAGER</p>

    <h2 class="side-heading" style="top:336px">About me</h2>
    <div class="side-rule" style="top:372px;width:215px"></div>
    <div class="about-text">
      <p>My Name Is Owen Marsh lorem empus id fringilla molestie ornare diam in olestie ipsum etium rosn ollicitudin est, porttitor amet hitmassa Done cporttitor dolor shit dolor kiren lorem nisl molestie pretium etfring. is the shitp lorem ipcum retiumci amet is tudinest.moles tium lorem olestie pretium apaza all the rosen. fringilla lorem ipsum .</p>
      <p>orem nisl molestie pretium etfring. is the shitp lorem ipcum retiumci amet is tudinest.moles tium lorem olestie pretium apaza all the rosen. fringilla</p>
    </div>

    <h2 class="side-heading" style="top:676px">Language</h2>
    <div class="side-rule" style="top:716px;width:199px"></div>
    <ul class="language-list">
      <li><span>English</span><span>70%</span></li>
      <li><span>Spanish</span><span>50%</span></li>
      <li><span>Arabic</span><span>30%</span></li>
    </ul>

    <h2 class="side-heading" style="top:809px">Contact</h2>
    <div class="side-rule" style="top:854px;width:199px"></div>
    <ul class="contact-list">
      <li>Year, Month/Date</li>
      <li>Your City, Country</li>
      <li>123 - 456 -78</li>
      <li>hello@example.com</li>
    </ul>

    <div class="company-mark">
      <span class="mark-square"></span>
      <span class="mark-name">KTW</span>
    </div>

    <h2 class="section-heading" style="top:305px">
      <svg viewBox="0 0 28 28" aria-hidden="true">
        <circle cx="14" cy="14" r="14" fill="var(--core-blue)"/>
        <rect x="7" y="10" width="14" height="10" rx="1.5" fill="none" stroke="#fff" stroke-width="1.8"/>
        <path d="M11 10 V8 H17 V10" fill="none" stroke="#fff" stroke-width="1.8"/>
        <line x1="7" y1="14.5" x2="21" y2="14.5" stroke="#fff" stroke-width="1.5"/>
        <rect x="12.5" y="13.3" width="3" height="2.6" fill="#fff"/>
      </svg>
      Work Experience
    </h2>
    <div class="section-rule" style="top:346px"></div>

    <div class="entry" style="top:367px">
      <span class="label">LOREM IPSUM</span><span class="years">2015 - 2017</span>
      <span class="role">Lorem Ipsum Design Studios</span>
      <p class="detail">Porttitor amet massa Done cporttitor dolor et nisl molestie ium feliscon lore ipsum dolor tfringilla. lorem lorem ipsum. ollcitudin est dolor time. Done cporttitor dolor kiren</p>
    </div>
    <div class="entry" style="top:454px">
      <span class="label">LOREM IPSUM</span><span class="years">2013 - 2015</span>
      <span class="role">Lorem Ipsum Ltd</span>
      <p class="detail">Porttitor amet massa Done cporttitor dolor et nisl molestie ium feliscon lore ipsum dolor tfringilla. lorem lorem ipsum. ollcitudin est dolor time.</p>
    </div>
    <div class="entry" style="top:541px">
      <span class="label">LOREM IPSUM</span><span class="years">2010 - 2013</span>
      <span class="role">Lorem IpsumSolutions</span>
      <p class="detail">Porttitor amet massa Done cporttitor dolor et nisl molestie ium feliscon lore ipsum dolor tfringilla. lorem lorem ipsum. ollcitudin est dolor time. Done cporttitor</p>
    </div>
    <div class="entry" style="top:628px">
      <span class="label">LOREM IPSUM</span><span class="years">2009 - 2010</span>
      <span class="role">Lorem Ipsum Creative</span>
      <p class="detail">Porttitor amet massa Done cporttitor dolor et nisl molestie ium feliscon lore ipsum dolor tfringilla. lorem lorem ipsum. ollcitudin est dolor time. Done cporttitor</p>
    </div>

    <h2 class="section-heading" style="top:703px;left:341px">
      <svg viewBox="0 0 28 28" aria-hidden="true">
        <circle cx="14" cy="14" r="14" fill="var(--core-blue)"/>
        <path d="M5 12 L14 8 L23 12 L14 16 Z" fill="#fff"/>
        <path d="M9 14 V19 C11 21 17 21 19 19 V14 L14 16.5 Z" fill="none" stroke="#fff" stroke-width="1.6"/>
      </svg>
      Education
    </h2>
    <div class="section-rule" style="top:746px"></div>

    <div class="entry education" style="top:765px">
      <span class="label">University of Lorem</span><span class="years">2008 - 2010</span>
      <span class="role">Certificate Lorem Ipsum Trainig</span>
      <p class="detail">Porttitor amet massa Done cporttitor dolor et nisl molestie ium feliscon lore ipsum dolor tfringilla. lorem lorem ipsum. ollcitudin est dolor time.</p>
    </div>
    <div class="entry education" style="top:846px">
      <span class="label">University of Lorem</span><span class="years">2007 - 2009</span>
      <span class="role">Lorem Ipsum Art Director</span>
      <p class="detail">Porttitor amet massa Done cporttitor dolor et nisl molestie ium feliscon lore ipsum dolor tfringilla. lorem lorem ipsum. ollcitudin est dolor time. Done cporttitor</p>
    </div>
    <div class="entry education" style="top:928px">
      <span class="label">University of Lorem</span><span class="years">2007 - 2009</span>
      <span class="role">Lorem IpsumArt Director</span>
      <p class="detail">Porttitor amet massa Done cporttitor dolor et nisl molestie ium feliscon lore ipsum dolor tfringilla. lorem lorem ipsum. ollcitudin est dolor time. Done cporttitor</p>
    </div>
    <div class="entry education" style="top:1009px">
      <span class="label">University of Lorem</span><span class="years">2007 - 2009</span>
      <span class="role">Bechelor Lorem Ipsum</span>
      <p class="detail">Porttitor amet massa Done cporttitor dolor et nisl molestie ium feliscon lore ipsum dolor tfringilla. lorem lorem ipsum. ollcitudin est dolor time. Done cporttitor</p>
    </div>
  </main>
</body>
</html>
```